Stonebell Inc Ad Design, trying to attract new customers

Please see attached pictures and files for information
We are a Class A - Residential General Contractor in Lynchburg, VA with Master HVAC and Master PLUMBING Licenses. We focus on Water and Air Solutions for property owners.
We build, remodel, and repair homes
We do HVAC, including Humidity Control and Air Purification
We do Plumbing
We love to fix Water Leaks for Plumbing, Roof Leaks, Skylight Leaks, Basement Leaks, Foundation Leaks, Door and Window Leaks
We solve water and air issues on the outside of properties with custom structures, grading, and landscaping

Target Market(s)

Residential and Light Commercial property owners

Industry/Entity Type

Construction

Font styles to use
Other font styles liked:
• see cards

Colors
0054AA
0677BA
7BADD7
CADEEF
E8F1F8
00AB8E
00BBA5
67D7C9
C6EFE9
E9F9F6

Requirements
Must have
• See business cards
Nice to have
• see business cards
Should not have
• My name

```html
<!DOCTYPE html>
<html lang="en">
<head>
<meta charset="utf-8">
<title>Stonebell Inc – Water and Air Banner</title>
<link rel="stylesheet" href="https://fonts.googleapis.com/css2?family=Oswald:wght@700&family=Roboto:ital,wght@0,400;0,500;1,900&display=swap">
<style>
  :root {
    --page-bg: #cccbca;
    --card-bg: #ffffff;
    --brand-blue: #0a9ee0;
    --brand-green: #6cb33f;
    --chip-border: #2aa8d4;
    --ink: #111111;
    --label-bg: #000000;
    --photo-deep: #0a6f9c;
    --photo-light: #1b9fd6;
  }
  * { box-sizing: border-box; margin: 0; padding: 0; }
  html, body { width: 1003px; height: 1200px; overflow: hidden; }
  body { background: var(--page-bg); position: relative; font-family: "Roboto", sans-serif; }

  .banner {
    position: absolute; left: 67px; top: 365px;
    width: 868px; height: 434px;
    background: var(--card-bg);
    overflow: hidden;
    box-shadow: 0 4px 8px rgba(0,0,0,0.18);
  }

  .photo-panel { position: absolute; left: 0; top: 0; width: 868px; height: 434px; }

  .headline {
    position: absolute; left: 19px; top: 18px;
    font-family: "Oswald", sans-serif; font-weight: 700;
    font-size: 64px; line-height: 71px;
    color: var(--brand-blue); letter-spacing: 0.5px;
  }
  .headline .accent {
    background: linear-gradient(90deg, var(--brand-blue) 0%, var(--brand-green) 55%);
    -webkit-background-clip: text; background-clip: text;
    color: transparent;
  }

  .license-label {
    position: absolute; left: 19px; top: 245px;
    width: 342px; height: 29px; border-radius: 4px;
    background: var(--label-bg); color: #fff;
    font-weight: 900; font-style: italic; font-size: 19px;
    line-height: 29px; padding-left: 11px;
  }

  .service {
    position: absolute; height: 28px;
    border: 1px solid var(--chip-border); border-radius: 4px;
    font-size: 10px; font-weight: 500; color: var(--ink);
    line-height: 26px; padding-left: 8px; white-space: nowrap;
  }

  .contact { position: absolute; top: 370px; display: flex; align-items: center; }
  .contact-icon { width: 34px; height: 34px; }
  .contact-text { font-size: 18px; color: var(--ink); }
  .contact-phone { left: 25px; }
  .contact-phone .contact-text { margin-left: 6px; }
  .contact-email { left: 210px; }
  .contact-email .contact-text { margin-left: 15px; }

  .brand {
    position: absolute; left: 467px; top: 40px;
    display: flex; align-items: center; gap: 6px;
  }
  .brand-dot { width: 12px; height: 12px; border-radius: 50%; background: var(--brand-green); }
  .brand-name {
    font-family: "Roboto", sans-serif; font-weight: 500;
    font-size: 20px; letter-spacing: 1.5px; color: var(--brand-blue);
  }
</style>
</head>
<body>
  <section class="banner">
    <svg class="photo-panel" viewBox="0 0 868 434" role="img" aria-label="Photo of a smiling tradesman in green coveralls and a tool belt, gesturing with an open hand, over a blue plumbing background">
      <defs>
        <linearGradient id="photoTone" x1="0" y1="0" x2="1" y2="1">
          <stop offset="0" stop-color="var(--photo-light)"/>
          <stop offset="1" stop-color="var(--photo-deep)"/>
        </linearGradient>
      </defs>
      <polygon points="638,0 868,0 868,434 559,434" fill="url(#photoTone)"/>
    </svg>

    <h1 class="headline">
      WE <span class="accent">PUT</span><br>
      WATER AND AIR<br>
      IN ITS <span class="accent">PLACE</span>
    </h1>

    <div class="brand">
      <span class="brand-dot"></span>
      <span class="brand-name">STONEBELL</span>
    </div>

    <p class="license-label">Class A RBC PLUMBINGHVAC</p>

    <div class="service" style="left:19px;top:285px;width:174px;">Humidity Control/Air Purification,</div>
    <div class="service" style="left:199px;top:285px;width:174px;padding-left:16px;">Roof/Skylight Leaks,</div>
    <div class="service" style="left:380px;top:286px;width:174px;">Drainage/Grading/Landscaping,</div>
    <div class="service" style="left:21px;top:320px;width:174px;padding-left:10px;">Basement/Foundation Leaks,</div>
    <div class="service" style="left:202px;top:320px;width:354px;padding-left:11px;">Custom Outdoor Structures - Porches, Decks, Sunrooms, Gazebos</div>

    <div class="contact contact-phone">
      <svg class="contact-icon" viewBox="0 0 34 34" aria-hidden="true">
        <defs>
          <linearGradient id="iconTone" x1="0" y1="0" x2="1" y2="1">
            <stop offset="0" stop-color="var(--brand-blue)"/>
            <stop offset="1" stop-color="var(--brand-green)"/>
          </linearGradient>
        </defs>
        <circle cx="17" cy="17" r="17" fill="url(#iconTone)"/>
        <path d="M11 9c1-.8 2-.6 2.6.4l1.6 2.6c.5.9.3 1.7-.5 2.3l-1 .8c.8 2 2.4 3.7 4.3 4.6l.8-1c.6-.8 1.5-1 2.3-.5l2.6 1.6c1 .6 1.1 1.7.3 2.6l-1.3 1.4c-1 1-2.7 1.2-4.6.3-3.4-1.6-6.3-4.6-7.8-8-.8-1.9-.6-3.6.4-4.6z" fill="#fff"/>
      </svg>
      <span class="contact-text">(434) 555-0172</span>
    </div>

    <div class="contact contact-email">
      <svg class="contact-icon" viewBox="0 0 34 34" aria-hidden="true">
        <circle cx="17" cy="17" r="17" fill="url(#iconTone)"/>
        <rect x="9" y="12" width="16" height="11" fill="none" stroke="#fff" stroke-width="1.4"/>
        <path d="M9 12l8 6 8-6M9 23l6-5M25 23l-6-5" fill="none" stroke="#fff" stroke-width="1.2"/>
      </svg>
      <span class="contact-text">Contact@StonebellVA.com</span>
    </div>
  </section>
</body>
</html>
```